26 HarborSparks, quotes who will inspire entrepreneurs when create new startups

This project is about 26 quotes that I wrote about create startups, my intention is to share and to inspire another founders o think about theses 26 things before or after create your company. It must be clear, beautiful, with a great design and easy to read, but with strong visual impact. It also important to highlight some powerfull word in each slide, giving something for the audience to remember in each quote

Target Market(s)

Entrepreneurs, investors, startup founders, acelerators

Industry/Entity Type

Startup

Font styles to use
Sans Serif

Colors
f37122
f78f20
fece3e
ffc214
fbed22
fbee3d
8dcce8
33a6d7
0692cd

Requirements
Must have
• Great type and font design, impact, lots of colors
Nice to have
• different fonts, clear message, inspirational
Should not have
• photos,

```html
<!DOCTYPE html>
<html lang="en">
<head>
<meta charset="utf-8">
<title>26 HarborSparks</title>
<link href="https://fonts.googleapis.com/css2?family=Montserrat:wght@200;300;400;600;700;800;900&display=swap" rel="stylesheet">
<style>
  :root {
    --orange: #f7931f;
    --orange-deep: #f37122;
    --red: #e9401b;
    --blue: #0692cd;
    --blue-mid: #33a6d7;
    --white: #ffffff;
    --ink: #4a4a4a;
    --page: #ffffff;
  }
  * { margin: 0; padding: 0; box-sizing: border-box; }
  html, body { width: 1200px; height: 1200px; overflow: hidden; background: var(--page); }
  body { position: relative; font-family: "Montserrat", sans-serif; }

  .slide {
    position: absolute; left: 88px; width: 1024px; height: 576px;
    background: var(--white); overflow: hidden;
    box-shadow: 0 3px 8px rgba(0,0,0,0.28);
  }
  .slide--cover { top: 12px; }
  .slide--quote { top: 612px; }

  .brand {
    position: absolute; color: var(--white);
    font-weight: 600; font-size: 11px; letter-spacing: 0.5px;
    display: flex; align-items: center; gap: 5px;
  }
  .brand__dot { width: 8px; height: 8px; border-radius: 50%; background: var(--white); }

  /* cover */
  .cover__band { position: absolute; left: 0; top: 0; width: 100%; height: 380px; background: var(--orange); }
  .cover__brand { left: 72px; top: 70px; }
  .cover__title {
    position: absolute; right: 50px; top: 128px;
    color: var(--white); font-weight: 700; font-size: 80px; letter-spacing: 1px; line-height: 1;
  }
  .cover__subtitle {
    position: absolute; right: 50px; top: 218px;
    color: var(--white); font-weight: 200; font-size: 29px; letter-spacing: 0.5px;
  }
  .cover__portrait {
    position: absolute; left: 52px; top: 264px; width: 250px; height: 250px;
    border-radius: 50%; border: 10px solid var(--white);
    background: radial-gradient(circle at 50% 40%, #b9a59a 0%, #9c9aa3 45%, #c9d0dc 100%);
  }
  .cover__name {
    position: absolute; left: 306px; top: 404px;
    color: var(--ink); font-weight: 400; font-size: 26px; letter-spacing: 1px;
  }
  .cover__role {
    position: absolute; left: 306px; top: 434px;
    color: var(--orange); font-weight: 300; font-size: 14px;
  }

  /* quote slide */
  .quote__brand-box {
    position: absolute; left: 51px; top: 1px; width: 119px; height: 119px;
    background: var(--orange); display: flex; align-items: center; justify-content: center;
  }
  .quote__brand-box .brand { position: static; font-size: 10px; }
  .quote__figure {
    position: absolute; left: 168px; top: 80px; width: 228px; height: 416px;
    border-radius: 110px 110px 30px 30px;
    background: linear-gradient(90deg, #2f8fd6 0%, #e9eef5 22%, #e0a27a 45%, #d98d66 65%, #3f88d0 100%);
  }
  .quote__line {
    position: absolute; left: 420px; width: 420px; text-align: center; line-height: 1; white-space: nowrap;
  }
  .quote__be    { top: 90px;  color: var(--red); font-weight: 900; font-size: 60px; }
  .quote__nice  { top: 140px; color: var(--red); font-weight: 900; font-size: 60px; }
  .quote__person{ top: 194px; color: var(--red); font-weight: 900; font-size: 60px; }
  .quote__lead  { top: 256px; color: var(--blue); font-weight: 200; font-size: 25px; }
  .quote__your  { top: 266px; color: var(--red); font-weight: 300; font-size: 70px; }
  .quote__company { top: 326px; color: var(--red); font-weight: 300; font-size: 70px; letter-spacing: 1px; }
  .quote__show  { top: 400px; left: 392px; width: 500px; color: var(--blue); font-weight: 900; font-size: 81px; }
  .quote__number {
    position: absolute; left: 926px; top: 460px; width: 98px; height: 86px;
    background: var(--orange); color: var(--white);
    font-weight: 700; font-size: 40px; display: flex; align-items: center; justify-content: center;
  }
</style>
</head>
<body>
  <section class="slide slide--cover">
    <div class="cover__band"></div>
    <div class="brand cover__brand"><span class="brand__dot"></span>HARBORSPARKS</div>
    <h1 class="cover__title">26 HarborSparks</h1>
    <p class="cover__subtitle">Things to know before or after you create your startup</p>
    <div class="cover__portrait" role="img" aria-label="Portrait photo of the author"></div>
    <p class="cover__name">Dario Venkell</p>
    <p class="cover__role">Founder &amp; CEO HarborSparks</p>
  </section>

  <section class="slide slide--quote">
    <div class="quote__brand-box"><div class="brand"><span class="brand__dot"></span>HARBORSPARKS</div></div>
    <div class="quote__figure" role="img" aria-label="Illustration of a surfer holding a blue surfboard"></div>
    <p class="quote__line quote__be">Be</p>
    <p class="quote__line quote__nice">a nice</p>
    <p class="quote__line quote__person">person.</p>
    <p class="quote__line quote__lead">You are the first feature that</p>
    <p class="quote__line quote__your">your</p>
    <p class="quote__line quote__company">company</p>
    <p class="quote__line quote__show">Will show</p>
    <div class="quote__number">1</div>
  </section>
</body>
</html>
```